Guarding One's Body Using Sharp Steel Cover

Hi we are producing a self defense course entitled Guarding One's Body Using Sharp Steel: A Complete Manual For Learning The Finest And Handiest Wilderness Tool In Recorded History.

I listed this as a book cover but it will actually be a DVD set, but the book cover model works fine.

See below for design examples - I am thinking we need a cover that will appeal to military/survival type people.

Target Market(s)

survivalists, cops, preppers, gun owners, martial artists, and average people wanting to learn how to defend themselves

Industry/Entity Type

Defense

Requirements
Must have
• Title: GUARDING ONE'S BODY USING SHARP STEEL: A COMPLETE MANUAL FOR LEARNING THE FINEST AND HANDIEST WILDERNESS TOOL IN RECORDED HISTORY
Nice to have
• Please look at these sample designs from other books as a model:
• https://files.plorvexa.org/media/en/4/27/BrindelQXMP.jpg - This stye is ideal.
• Other good examples:
• https://pics2.talvorn.com/8143907_k370.jpg
• http://m.zephquill.com/titles/2719058463k/48071935.jpg
• http://img.crondelmart.com/pics/P/73Tm58QyzFr._BX_KL410_TR316,410_.jpg
• http://3.cdn.wendoplix.net/-RTyZWLMMKAQ/BNWq_hufxaT/BBBBBBBBv8G/DKNp815ZaXW/s1600/Q4710392.JPG

```html
<!DOCTYPE html>
<html lang="en">
<head>
<meta charset="utf-8">
<title>Guarding One's Body Using Sharp Steel – Cover</title>
<link rel="stylesheet" href="https://fonts.googleapis.com/css2?family=Anton&family=Arimo:wght@400;700&display=swap">
<style>
  :root {
    --stage: #d9d8d3;
    --cover-green: #5e6b3a;
    --cover-green-dark: #4c5830;
    --cover-green-light: #6d7a47;
    --band-black: #0d0e0b;
    --band-text: #6f7b3e;
    --title-white: #ecebe4;
    --photo-light: #b7bd9a;
    --photo-mid: #8f9870;
  }
  * { box-sizing: border-box; margin: 0; padding: 0; }
  html, body {
    width: 1200px;
    height: 789px;
    overflow: hidden;
    background: var(--stage);
  }
  .canvas {
    position: relative;
    width: 1200px;
    height: 789px;
  }
  .cover {
    position: absolute;
    left: 350px;
    top: 30px;
    width: 500px;
    height: 729px;
    overflow: hidden;
    background:
      radial-gradient(ellipse at 30% 40%, var(--cover-green-light) 0%, transparent 60%),
      radial-gradient(ellipse at 80% 90%, var(--cover-green-dark) 0%, transparent 55%),
      var(--cover-green);
    box-shadow: 0 6px 22px rgba(0,0,0,0.25);
  }
  .series-band {
    position: absolute;
    left: 0; top: 0;
    width: 100%;
    height: 80px;
    background: var(--band-black);
    padding: 12px 22px 0;
  }
  .series-band p {
    font-family: "Arimo", sans-serif;
    font-size: 17px;
    line-height: 19px;
    letter-spacing: 0.5px;
    color: var(--band-text);
    text-transform: uppercase;
    white-space: nowrap;
  }
  .cover-photo {
    position: absolute;
    right: 0;
    bottom: 0;
    width: 310px;
    height: 370px;
    background:
      radial-gradient(ellipse at 55% 30%, var(--photo-light) 0%, var(--photo-mid) 45%, transparent 80%);
    opacity: 0.85;
  }
  .title {
    position: absolute;
    left: 62px;
    top: 112px;
    color: var(--title-white);
  }
  .title .minor {
    display: block;
    font-family: "Arimo", sans-serif;
    font-size: 34px;
    line-height: 40px;
    letter-spacing: 0.5px;
  }
  .title .major {
    display: block;
    font-family: "Anton", sans-serif;
    font-size: 98px;
    line-height: 92px;
    letter-spacing: 1px;
    text-transform: uppercase;
  }
  .title .minor.indent { padding-left: 120px; }
</style>
</head>
<body>
  <main class="canvas">
    <section class="cover">
      <header class="series-band">
        <p>A Complete Manual For Learning</p>
        <p>The Finest And Handiest Wilderness</p>
        <p>Tool In Recorded History</p>
      </header>

      <div class="cover-photo" role="img" aria-label="Photo of one hand gripping a raised fixed-blade knife while another hand grabs the wrist, tinted green"></div>

      <h1 class="title">
        <span class="minor">Guarding One's</span>
        <span class="major">Body</span>
        <span class="major">Using</span>
        <span class="minor indent">sharp</span>
        <span class="major">Steel</span>
      </h1>
    </section>
  </main>
</body>
</html>
```